Nonprofit Postcard Design

We need a postcard designed to raise awareness and donations for a Nonprofit called "RMW Memorial". We are a new nonprofit that gives out scholarships to high school seniors. In 2005 my brother, Ronald Miles Wendover, was taken from my family in a violent act of crime. My family has formed a scholarship foundation, RMW Memorial Scholarship, in memory of my brother. This scholarship fund will help seniors who want to go to college by giving them money that can aide in the cost of books, tuition, or housing. We would like to give two scholarships per year, and we need your help to make that possible. Ron was a loving and very kind person who would help anyone who needed it. He was a member of the Bell Ridge High School Band and a very academically involved student who planned to go to college. We are remembering him through this scholarship. We are a non-profit organization, so all donations are tax deductible. Each year, students will receive a scholarship, along with a certificate which will list all company logos that have donated to make this scholarship one that can last for many years to come. www.rmwmemorial.example

Industry/Entity Type

High School

```html
<!DOCTYPE html>
<html lang="en">
<head>
<meta charset="utf-8">
<title>RMW Memorial Scholarship – Postcard</title>
<link rel="stylesheet" href="https://fonts.googleapis.com/css2?family=Bitter:ital,wght@1,700&family=Mulish:wght@400;700&display=swap">
<style>
  :root {
    --navy: #23405f;
    --navy-panel: #26405d;
    --slate-panel: #44566e;
    --bar: #3b5877;
    --sky-top: #8fc1e4;
    --sky-mid: #c9e1f1;
    --sky-low: #eaf4fa;
    --text-dark: #3a3a3a;
    --yellow: #f1e01f;
    --white: #ffffff;
    --rule: #3a3a3a;
    --card-edge: #c9c9c9;
  }
  * { box-sizing: border-box; margin: 0; padding: 0; }
  html, body { width: 849px; height: 1200px; overflow: hidden; background: var(--white); }
  body { position: relative; font-family: "Mulish", sans-serif; color: var(--text-dark); }

  .card { position: absolute; left: 66px; width: 729px; border: 1px solid var(--card-edge); overflow: hidden; background: var(--white); }
  .card--front { top: 23px; height: 562px; }
  .card--back { top: 600px; height: 566px; }

  .abs { position: absolute; }

  /* front */
  .front-sky { inset: 0; background: linear-gradient(180deg, var(--sky-top) 0%, var(--sky-mid) 45%, var(--sky-low) 100%); }
  .headline { left: 48px; top: 64px; font-family: "Bitter", serif; font-style: italic; font-weight: 700; font-size: 25px; color: var(--navy); white-space: nowrap; }
  .graduates-photo { left: 252px; top: 100px; width: 477px; height: 240px;
    background: linear-gradient(90deg, rgba(143,193,228,0) 0%, #3a3a44 14%, #7a1f24 30%, #2a2a30 48%, #8a2228 66%, #26262c 84%, #3a3a44 100%); }
  .photo-bar { left: 269px; top: 340px; width: 460px; height: 13px; background: linear-gradient(90deg, #6f8aa6, var(--bar) 30%); }
  .brand { display: flex; align-items: center; gap: 8px; color: var(--navy); font-family: "Mulish", sans-serif; font-weight: 700; }
  .brand-mark { flex: none; border-radius: 50%; background: var(--navy); }
  .brand--front { left: 34px; top: 370px; width: 220px; font-size: 21px; line-height: 1.2; }
  .brand--front .brand-mark { width: 22px; height: 22px; }
  .org-title { left: 270px; top: 384px; width: 444px; text-align: center; font-family: "Bitter", serif; font-style: italic; font-weight: 700; font-size: 26px; color: var(--navy); white-space: nowrap; }
  .org-intro { left: 286px; top: 432px; width: 420px; text-align: center; font-size: 14.5px; line-height: 20px; color: var(--text-dark); white-space: nowrap; }
  .site-url { left: 66px; top: 508px; font-size: 14.5px; color: var(--text-dark); white-space: nowrap; }

  /* back */
  .back-sky { left: 0; top: 0; width: 549px; height: 181px; background: linear-gradient(180deg, #b6d6ec 0%, var(--sky-mid) 40%, var(--sky-low) 100%); }
  .brand--back { left: 30px; top: 70px; width: 180px; font-size: 17px; line-height: 1.2; }
  .brand--back .brand-mark { width: 18px; height: 18px; }
  .contact { left: 232px; top: 36px; width: 305px; font-size: 15px; line-height: 20px; color: var(--text-dark); white-space: nowrap; }
  .contact-name { font-family: "Bitter", serif; font-style: italic; font-weight: 700; font-size: 19px; color: var(--navy); margin-bottom: 6px; }
  .contact-gap { height: 20px; }
  .stamp-box { left: 558px; top: 26px; width: 113px; height: 139px; border: 2px dotted #555; }

  .donate-panel { left: 0; top: 181px; width: 353px; height: 266px; background: var(--navy-panel); }
  .donate-call { right: 18px; top: 27px; width: 330px; text-align: right; color: var(--white); font-weight: 700; font-size: 16px; line-height: 22px; white-space: nowrap; }
  .mail-to { right: 18px; top: 91px; text-align: right; color: var(--white); font-weight: 700; font-size: 16px; line-height: 20.5px; white-space: nowrap; }
  .tax-note { right: 18px; top: 196px; text-align: right; color: var(--yellow); font-weight: 700; font-size: 16px; line-height: 20.5px; white-space: nowrap; }
  .donation-art { left: 2px; top: 102px; width: 160px; height: 141px;
    background: linear-gradient(180deg, #5f6d6a 0%, #c7a873 40%, #e9dcc2 60%, #3d6fb3 80%, #2a2d3e 100%); border-radius: 4px; }

  .certificate-panel { left: 0; top: 447px; width: 353px; height: 119px; background: var(--slate-panel); }
  .certificate-note { left: 0; top: 12px; width: 353px; text-align: center; color: var(--white); font-size: 13px; line-height: 16.5px; white-space: nowrap; }

  .address-lines { left: 399px; top: 285px; width: 304px; }
  .address-lines span { display: block; height: 44px; border-bottom: 1.5px solid var(--rule); }
  .address-lines span:first-child { height: 1px; }
</style>
</head>
<body>

<section class="card card--front" aria-label="Postcard front">
  <div class="abs front-sky" role="img" aria-label="Soft blue sky with light clouds"></div>
  <h1 class="abs headline">Help Them To Realise Their Dreams ...</h1>
  <div class="abs graduates-photo" role="img" aria-label="Photo of graduates in caps and gowns seen from behind"></div>
  <div class="abs photo-bar"></div>
  <div class="abs brand brand--front"><span class="brand-mark"></span><span>RMW Memorial Scholarship</span></div>
  <h2 class="abs org-title">RMW Memorial Nonprofit</h2>
  <p class="abs org-intro">
    We are a local Nonprofit that is dedicated to give back<br>
    to the local community, In Loving memory of Ronald Wendover<br>
    At RMW Memorial, we are focused on providing<br>
    East Texas high school seniors with scholarships for<br>
    higher education.
  </p>
  <p class="abs site-url">www.rmwmemorial.example</p>
</section>

<section class="card card--back" aria-label="Postcard back">
  <div class="abs back-sky" role="img" aria-label="Pale sky band"></div>
  <div class="abs brand brand--back"><span class="brand-mark"></span><span>RMW Memorial Scholarship</span></div>
  <div class="abs contact">
    <p class="contact-name">RMW Memorial Nonprofit Corp.</p>
    <p>Email : MWendover@rmwmemorial.example</p>
    <div class="contact-gap"></div>
    <p>Address : PO Box 4417</p>
    <p>Bell Ridge, TX 75590</p>
  </div>
  <div class="abs stamp-box" aria-label="Stamp area"></div>

  <div class="abs donate-panel">
    <p class="abs donate-call">Give back to the community by donating<br>to the RMW Memorial Scholarship Fund.</p>
    <div class="abs donation-art" role="img" aria-label="Illustration of a coin jar on a stack of books with an open book"></div>
    <p class="abs mail-to">Mail Donations to:<br>RMW Memorial<br>P.O. Box 4417<br>Bell Ridge TX 75590</p>
    <p class="abs tax-note">All Donations are<br>Tax-deductible!!</p>
  </div>

  <div class="abs certificate-panel">
    <p class="abs certificate-note">
      Each year, students will receive a scholarship,<br>
      along with a certificate which will list all company<br>
      logos that have donated to make this<br>
      scholarship one that can last for many years<br>
      to come
    </p>
  </div>

  <div class="abs address-lines" aria-hidden="true">
    <span></span><span></span><span></span><span></span>
  </div>
</section>

</body>
</html>
```